Design a Website Mockup for educational online magazine for children

Dear Freelance designers,

We are a child-focused charity looking for a creative design for an educational online magazine for children that will learn about other cultures by watching videos, photos and reading other media created by children from all around the world.

Some of the requirements:

- Target audience is children 10-12 years of age from different countries
- Online magazine will be built using open source Drupal CMS (examples of Drupal magazines include: http://www.quillgazette.example/ or you can view more examples at http://www.sitepavilion.example/categories-listing/Magazines%20%26%20Journals )
- We like clean and uncluttered designs
- We like large buttons and call to action areas
- We like a design that looks playful and almost handmade
- Vivid, bright colours (making strong use of one or more of KiteNest’s primary or secondary colours). Colours will also have to adhere to accessibility guidelines. primary and secondary colours guidelines can be found here: https://www.filecrate.example/s/pq7mnzt3rx81a2b/Primary%20and%20secondary%20colours.pdf
- Wireframes can be seen here: https://www.filecrate.example/s/hx4tq92lw06y5ze/Online%20Magazine%20-%20wireframes.pdf or also attached

Other available materials:

- Logo of program that you can find here: https://www.filecrate.example/s/3rnbe8kvo51gmdu/kitenest_logo.png
- Full branding guidelines can be found here: https://www.filecrate.example/s/b7zwq314pkn82tc/Branding%20Guidelines.pdf
- You can use photos from (http://www.friendwall.example/kitenestaustralia) or from http://kitenestlink.example/explore (you are not allowed to use photos for any other purpose that for this contest)

Your submission should include:
- At least 2 mockups that show 1 or more pages from the online magazine website
- Short explanation of your approach to the brief.
- If you can, please provide a mockup of how homepage would look on mobile

Winning entry will be selected based on:

- Design follows the requirements explained above
- Design can be implemented using a PHP based content management system like Drupal
- Design follows the wireframe(s) structure
- Design follows branding guidelines

```html
<!DOCTYPE html>
<html lang="en">
<head>
<meta charset="utf-8">
<title>KiteNest Connect – Children's Magazine</title>
<link href="https://fonts.googleapis.com/css2?family=Days+One&family=Varela+Round&display=swap" rel="stylesheet">
<style>
  :root{
    --leaf:#a6cf3d;
    --leaf-pale:#c7e4a3;
    --leaf-dark:#2b8a56;
    --sun:#f7a933;
    --sky:#2aa3e0;
    --peach:#fdd7a3;
    --lime:#e4ed98;
    --tile:#efefef;
    --ink:#333;
    --muted:#555;
    --white:#fff;
    --star-off:#c8c8c8;
  }
  *{box-sizing:border-box;margin:0;padding:0}
  html,body{width:1200px;height:2468px;overflow:hidden}
  body{position:relative;font-family:"Varela Round",sans-serif;color:var(--ink);background:var(--white)}
  .abs{position:absolute}

  .band-top{left:0;top:0;width:1200px;height:780px;background:linear-gradient(#c3e29c,#d7ecb8)}
  .band-videos{left:0;top:780px;width:1200px;height:780px;background:linear-gradient(var(--peach) 0%,#fde0b8 75%,#fff8ee 100%)}
  .band-photos{left:0;top:1560px;width:1200px;height:800px;background:linear-gradient(var(--lime) 0%,#eef4bf 80%,#fbfdf0 100%)}

  .brand{top:36px;width:170px;height:66px;display:flex;align-items:center;gap:8px;
    font-size:25px;color:var(--leaf-dark)}
  .brand-dot{width:18px;height:18px;border-radius:50%;background:var(--sun);flex:none}
  .brand.left{left:72px}
  .brand.right{left:966px}

  .main-nav{left:101px;top:156px;width:1002px;height:153px;display:flex;border:2px solid var(--white)}
  .main-nav a{flex:1;display:flex;align-items:center;justify-content:center;background:var(--tile);border-right:2px solid var(--white)}
  .main-nav a:last-child{border-right:0}
  .main-nav a.active{background:var(--sun)}
  .main-nav svg{width:104px;height:104px}

  .slider{left:32px;top:352px;width:818px;height:401px;background:#f3f3f3;border:2px solid #e2e2e2;border-radius:4px}
  .slide-art{left:13px;top:11px;width:788px;height:296px;background:linear-gradient(135deg,#e9eee4,#d8e6d0 50%,#eadfcf)}
  .slide-caption{left:13px;top:307px;width:788px;height:82px;background:var(--sun);padding:6px 25px;color:#4a3a1e}
  .slide-caption h2{font-weight:400;font-size:23px;line-height:1.1}
  .slide-caption p{font-size:15px;margin-top:2px}
  .dots{position:absolute;left:358px;bottom:6px;display:flex;gap:8px}
  .dots span{width:19px;height:19px;border-radius:50%;background:var(--white)}
  .dots span.on{background:var(--sky)}

  .magazine{left:881px;top:352px;width:282px;height:400px;background:var(--leaf);border-radius:4px}
  .search{left:11px;top:15px;width:208px;height:30px;background:var(--white);border:1px solid #ddd}
  .search-btn{left:223px;top:15px;width:48px;height:30px;background:var(--white);border:1px solid #ddd;display:flex;align-items:center;justify-content:center}
  .mag-cover{left:42px;top:60px;width:190px;height:201px;background:var(--white);border:1px solid #9ebf45}
  .mag-text{left:10px;top:282px;width:262px;text-align:center;font-size:16px;color:#3b4a1a;line-height:1.25}
  .start{left:22px;top:337px;width:234px;height:52px;background:var(--sun);border-radius:3px;display:flex;align-items:center;gap:34px;padding-left:18px;
    font-family:"Days One",sans-serif;font-size:28px;color:var(--white);letter-spacing:2px}

  .section-head{height:72px;background:var(--sky);color:var(--white);font-family:"Days One",sans-serif;font-size:36px;letter-spacing:3px;padding:14px 20px}
  .videos-head{left:31px;top:811px;width:818px}
  .photos-head{left:36px;top:1580px;width:817px}

  .item-title{font-size:19px;color:#3a3a3a}
  .card{width:396px;height:230px;background:var(--white);border-radius:5px;box-shadow:0 1px 3px rgba(0,0,0,.08)}
  .card .media{position:absolute;left:16px;top:18px;width:250px;height:194px}
  .card .meta{position:absolute;left:282px;top:22px;font-size:17px;line-height:35px;color:#333}
  .stars{font-size:19px;color:var(--sun);letter-spacing:1px;margin-top:10px}
  .stars .off{color:var(--star-off)}
  .player-bar{position:absolute;left:0;bottom:0;width:100%;height:14px;background:#f2f2f2;border-top:1px solid #ccc}
  .player-bar::after{content:"";position:absolute;left:24px;right:64px;top:6px;height:2px;background:#999}
  .player-bar::before{content:"";position:absolute;left:24px;width:70px;top:5px;height:4px;background:#222;z-index:1}
  .play{position:absolute;left:80px;top:46px;width:92px;height:92px}

  .side-box{background:#f2f2f2;border:1px solid #e6e6e6;padding:14px 20px;font-size:16px;color:#444;line-height:1.25}
  .quiz{left:880px;top:812px;width:280px;height:301px}
  .quiz ul{list-style:none;margin-top:14px}
  .quiz li{display:flex;align-items:center;height:35px;color:#555}
  .quiz li span{width:80px}
  .quiz li i{display:block;width:46px;height:20px;border:1px solid #999;background:var(--white)}
  .quiz .btn{position:absolute;left:22px;width:236px;height:53px;color:var(--white);font-size:23px;display:flex;align-items:center;justify-content:center;border-radius:3px}
  .quiz .submit{top:172px;background:#7cc043}
  .quiz .result{top:237px;background:var(--sun)}
  .fact{left:880px;top:1177px;width:280px;height:300px}
  .tips{left:880px;top:1583px;width:280px;height:300px}
  .side-box p{text-align:justify;margin-top:16px;font-size:16.5px;line-height:1.22}

  .footer{left:0;top:2360px;width:1200px;height:108px;background:var(--leaf-dark);display:flex}
  .footer > div{width:300px;border-right:2px solid #5cae7f;display:flex;flex-direction:column;align-items:center;justify-content:center;color:var(--white);font-size:17px;gap:6px}
  .footer > div:last-child{border-right:0}
  .footer .f-brand{font-size:40px;line-height:1;align-items:flex-start;padding-left:40px}
  .footer .f-brand small{font-size:15px;align-self:flex-end;margin-right:28px}
  .footer svg{width:60px;height:60px}
</style>
</head>
<body>

<div class="abs band-top"></div>
<div class="abs band-videos"></div>
<div class="abs band-photos"></div>

<div class="abs brand left"><span class="brand-dot"></span>KiteNest Connect</div>
<div class="abs brand right"><span class="brand-dot"></span>KiteNest Connect</div>

<nav class="abs main-nav">
  <a class="active" href="#" aria-label="Home">
    <svg viewBox="0 0 100 100" fill="none" stroke="#fff" stroke-width="7" stroke-linejoin="round" stroke-linecap="round"><path d="M12 48 L50 12 L88 48"/><path d="M22 40 V88 H40 V64 A10 10 0 0 1 60 64 V88 H78 V40"/><circle cx="50" cy="44" r="8"/></svg>
  </a>
  <a href="#" aria-label="Videos">
    <svg viewBox="0 0 100 100" fill="none" stroke="#2aa3e0" stroke-width="7" stroke-linejoin="round"><rect x="8" y="22" width="84" height="56" rx="8"/><path d="M40 36 L66 50 L40 64 Z" fill="#2aa3e0"/></svg>
  </a>
  <a href="#" aria-label="Photos">
    <svg viewBox="0 0 100 100" fill="none" stroke="#2aa3e0" stroke-width="7" stroke-linejoin="round"><path d="M10 30 H32 L38 18 H62 L68 30 H90 V84 H10 Z"/><circle cx="50" cy="56" r="18"/><circle cx="50" cy="56" r="8"/></svg>
  </a>
  <a href="#" aria-label="Write">
    <svg viewBox="0 0 100 100" fill="none" stroke="#2aa3e0" stroke-width="7" stroke-linejoin="round" stroke-linecap="round"><path d="M40 12 H16 V90 H76 V56"/><path d="M40 12 V34 H18"/><path d="M46 64 L50 50 L82 18 L92 28 L60 60 Z" fill="#2aa3e0"/></svg>
  </a>
  <a href="#" aria-label="World">
    <svg viewBox="0 0 100 100" fill="none" stroke="#2aa3e0" stroke-width="6" stroke-linecap="round"><circle cx="50" cy="42" r="28" fill="#2aa3e0"/><path d="M50 14 V70 M22 42 H78 M30 24 Q50 34 70 24 M30 60 Q50 50 70 60" stroke="#fff" stroke-width="3"/><path d="M20 52 A34 34 0 0 0 80 52"/><path d="M50 76 V88 M34 90 H66"/></svg>
  </a>
</nav>

<section class="abs slider">
  <div class="abs slide-art" role="img" aria-label="Children's poster drawing of two hands protecting a young seedling among small sprouts"></div>
  <div class="abs slide-caption">
    <h2>Save Trees</h2>
    <p>Winner of World Poster Competition,Name: Rana Devi, Country: Sri Lanka.</p>
    <div class="dots"><span></span><span class="on"></span><span></span><span></span></div>
  </div>
</section>

<aside class="abs magazine">
  <div class="abs search"></div>
  <div class="abs search-btn"><svg width="24" height="24" viewBox="0 0 24 24" fill="none" stroke="#2aa3e0" stroke-width="2.5"><circle cx="10" cy="10" r="6"/><path d="M15 15 L21 21"/></svg></div>
  <div class="abs mag-cover"></div>
  <p class="abs mag-text">Download Our Latest Printed Magazine</p>
  <div class="abs start"><svg width="46" height="40" viewBox="0 0 46 40" fill="none" stroke="#5a3a10" stroke-width="4"><path d="M23 2 V26 M13 16 L23 26 L33 16"/><path d="M4 24 V36 H42 V24"/></svg>START</div>
</aside>

<h2 class="abs section-head videos-head">LATEST VIDEOS</h2>

<p class="abs item-title" style="left:31px;top:908px">Street drowing in Summer Camp.</p>
<p class="abs item-title" style="left:453px;top:908px">What do you like to eat?</p>
<article class="abs card" style="left:31px;top:949px">
  <div class="media" role="img" aria-label="Video still: a girl chalk drawing on the pavement" style="background:linear-gradient(120deg,#6c6a66,#8b8680 60%,#a59b8e)">
    <svg class="play" viewBox="0 0 92 92"><circle cx="46" cy="46" r="40" fill="none" stroke="#a6cf3d" stroke-width="5"/><path d="M34 24 L72 46 L34 68 Z" fill="#7cc043"/></svg>
    <div class="player-bar"></div>
  </div>
  <div class="meta">Australia<br>Art<br>Oct,2013<div class="stars">★★★★<span class="off">★</span></div></div>
</article>
<article class="abs card" style="left:453px;top:949px">
  <div class="media" role="img" aria-label="Video title card asking what you like to eat" style="background:linear-gradient(160deg,#1a3fb0,#0c2a8f)">
    <svg class="play" viewBox="0 0 92 92"><circle cx="46" cy="46" r="40" fill="none" stroke="#a6cf3d" stroke-width="5"/><path d="M34 24 L72 46 L34 68 Z" fill="#7cc043"/></svg>
    <div class="player-bar"></div>
  </div>
  <div class="meta">Australia<br>Fooding<br>Oct,2013<div class="stars">★★★★<span class="off">★</span></div></div>
</article>

<p class="abs item-title" style="left:31px;top:1207px">My Family in a beach near home!!</p>
<p class="abs item-title" style="left:453px;top:1207px">Outing with friends, what you say?</p>
<article class="abs card" style="left:31px;top:1249px">
  <div class="media" role="img" aria-label="Video still: a family lying together on a sandy beach" style="background:linear-gradient(180deg,#cfd8dc,#e8dccb 60%,#d9c7ae)">
    <svg class="play" viewBox="0 0 92 92"><circle cx="46" cy="46" r="40" fill="none" stroke="#a6cf3d" stroke-width="5"/><path d="M34 24 L72 46 L34 68 Z" fill="#7cc043"/></svg>
    <div class="player-bar"></div>
  </div>
  <div class="meta">Vietnam<br>Holiday<br>Oct,2013<div class="stars">★★★★<span class="off">★</span></div></div>
</article>
<article class="abs card" style="left:453px;top:1249px">
  <div class="media" role="img" aria-label="Video still: friends jumping in silhouette at sunset" style="background:linear-gradient(180deg,#3d4a5c,#c98a3a 55%,#2b2620)">
    <svg class="play" viewBox="0 0 92 92"><circle cx="46" cy="46" r="40" fill="none" stroke="#a6cf3d" stroke-width="5"/><path d="M34 24 L72 46 L34 68 Z" fill="#7cc043"/></svg>
    <div class="player-bar"></div>
  </div>
  <div class="meta">India<br>Friends<br>Oct,2013<div class="stars">★★★★<span class="off">★</span></div></div>
</article>

<aside class="abs side-box quiz">
  How many sides a Triangle has?
  <ul>
    <li><span>a. Two</span><i></i></li>
    <li><span>b, Three</span><i></i></li>
    <li><span>c. Many</span><i></i></li>
  </ul>
  <div class="btn submit">Submit</div>
  <div class="btn result">See Result</div>
</aside>

<aside class="abs side-box fact">
  Did you know Why Japan is called “Land of Rising Sun”
  <p>Japan is called the land of the rising sun due to the fact that it is located at the eastern most part of Asia and is the closest to the world date line. The Japanese call Japan Nippon or Nihon which literally mean “the sun’s origin” hence being called the land of the rising sun.</p>
</aside>

<h2 class="abs section-head photos-head">LATEST PHOTOSTORIES</h2>

<p class="abs item-title" style="left:40px;top:1673px">I Cought a fish,Check this images!</p>
<p class="abs item-title" style="left:462px;top:1673px">Annual day with planting New Trees.</p>
<article class="abs card" style="left:31px;top:1716px">
  <div class="media" role="img" aria-label="Photo: a boy holding up a fish he caught" style="background:linear-gradient(160deg,#4a86c8,#8fb6d8 55%,#4f6a3a)"></div>
  <div class="meta">Australia<br>Fishing<br>Oct,2013<div class="stars">★★★★<span class="off">★</span></div></div>
</article>
<article class="abs card" style="left:453px;top:1716px">
  <div class="media" role="img" aria-label="Photo: schoolchildren in uniforms planting a tree" style="background:linear-gradient(180deg,#b9bfc4,#5b82b8 50%,#c8b090)"></div>
  <div class="meta">Srilanka<br>Event<br>Oct,2013<div class="stars">★★★★<span class="off">★</span></div></div>
</article>

<p class="abs item-title" style="left:40px;top:1972px">I help my mom,Everyday,Proud.</p>
<p class="abs item-title" style="left:462px;top:1972px">My Dance School.Guess me :).</p>
<article class="abs card" style="left:31px;top:2015px">
  <div class="media" role="img" aria-label="Photo: a girl washing pots outdoors" style="background:linear-gradient(160deg,#3b3a30,#6b6550 55%,#a8a59a)"></div>
  <div class="meta">India<br>Fooding<br>Oct,2013<div class="stars">★★★★<span class="off">★</span></div></div>
</article>
<article class="abs card" style="left:453px;top:2015px">
  <div class="media" role="img" aria-label="Photo: a group of young dancers in black leotards" style="background:linear-gradient(180deg,#8a8a80,#4a4a46 55%,#9a9286)"></div>
  <div class="meta">Australia<br>Dance<br>Oct,2013<div class="stars">★★★★<span class="off">★</span></div></div>
</article>

<aside class="abs side-box tips">
  Tips and Tricks
  <p>Study Alone Unless you've got a couple of friends who are super-serious about getting down to business, stay away from group study sessions because they tend to get off-topic pretty quickly. Save the social time till after you've handed in your test.</p>
</aside>

<footer class="abs footer">
  <div class="f-brand">KiteNest<small>Australia</small></div>
  <div>
    <svg viewBox="0 0 60 60" fill="none" stroke="#fff" stroke-width="3" stroke-linejoin="round"><path d="M18 6 H40 V54 H18 Z"/><path d="M30 30 H54 M38 22 L30 30 L38 38"/></svg>
    Privacy
  </div>
  <div>
    <svg viewBox="0 0 60 60" fill="none" stroke="#fff" stroke-width="3" stroke-linejoin="round"><path d="M6 24 H54 V54 H6 Z"/><path d="M6 24 L30 42 L54 24 M6 54 L24 38 M54 54 L36 38"/><path d="M30 30 V4 M22 12 L30 4 L38 12"/></svg>
    Contact
  </div>
  <div>
    <svg viewBox="0 0 60 60" fill="none" stroke="#fff" stroke-width="3.5" stroke-linecap="round"><circle cx="30" cy="30" r="26"/><path d="M22 23 A8 8 0 1 1 33 30 Q30 32 30 37"/><circle cx="30" cy="45" r="1.5" fill="#fff"/></svg>
    Help
  </div>
</footer>

</body>
</html>
```